Selling my Home Flyer

I need a flyer/brochure for a house listing I am putting together. I will put all of the information together for you to include in the flyer. This will only be a front and back flyer. No extra pages and no staples will be seen. This will be printed by a large office copier, not a professional copier on standard paper. Therefore no crazy dark backgrounds with lots of bleeding colors. Pictures that I want need for sure in there are Aerial with outline, Front from left, and one of the ones showing the large yard. I included a couple sample designs that I don't hate. But feel free to get creative. I will need this on a quick turnaround and I will make comments quickly as well, so submit ASAP.

Target Market(s)

People that will by my house.

Industry/Entity Type

Real Estate Agent

Font styles to use
Serif
Sans Serif

Colors

Designer to choose colors to be used in the design.

Requirements
Must have
• The pictures I mentioned above. And the price and SF and address! I forgot to tell you the address. It is 4817 Birchwell Lane, Palm Beach Gardens, FL 33410.
Should not have
• Anarchy. I don't want it to look too crazy. Should be pretty straight forward.

```html
<!DOCTYPE html>
<html lang="en">
<head>
<meta charset="utf-8">
<title>Selling My Home Flyer</title>
<link rel="stylesheet" href="https://fonts.googleapis.com/css2?family=Montserrat:wght@500;800&family=Oswald:wght@500;600&family=Tinos:wght@400;700&family=Roboto+Condensed:wght@400;500&display=swap">
<style>
  :root{
    --blue:#1b5aa0;
    --blue-deep:#14477f;
    --slate:#3c3d40;
    --ink:#0c0c0c;
    --paper:#ffffff;
    --stage:#e4e4e4;
    --logo-border:#c9ced6;
  }
  *{box-sizing:border-box;margin:0;padding:0}
  html,body{width:818px;height:1200px;overflow:hidden;background:var(--stage)}
  .canvas{position:relative;width:818px;height:1200px}
  .page{position:absolute;top:324px;width:440px;height:625px;background:var(--paper);
        transform:scale(.882);transform-origin:top left;box-shadow:0 3px 10px rgba(0,0,0,.25)}
  .page--front{left:10px}
  .page--back{left:420px}
  .block{position:absolute}
  .photo{position:absolute}
  .photo--garden{background:linear-gradient(180deg,#6f9fd6 0%,#b9c7a6 38%,#d9cdb3 52%,#4f8a3a 75%,#3f7a2c 100%)}
  .photo--porch{background:linear-gradient(90deg,#e9e6df 0%,#8b857a 40%,#cfcac0 70%,#6e6a62 100%)}
  .photo--aerial{background:linear-gradient(160deg,#3f6b2c 0%,#c9a184 40%,#8c9a7a 60%,#2f5a24 100%)}
  .photo--pool{background:linear-gradient(180deg,#4a6b3a 0%,#7c8f6a 35%,#5fc4d4 62%,#c49a80 85%,#b58a70 100%)}
  .photo--roofs{background:linear-gradient(90deg,#2f5a28 0%,#b65e46 35%,#4c7a36 60%,#c46a4f 100%)}
  .photo--facade{background:linear-gradient(180deg,#7fb1e6 0%,#cfc8b8 45%,#5f8c48 80%,#3f7030 100%)}
  .photo--living{background:linear-gradient(90deg,#e7dcc6 0%,#f3ede1 45%,#8a5a3c 85%,#6e4a34 100%)}
  .photo--room{background:linear-gradient(180deg,#e9e2d4 0%,#c8b89a 60%,#7a5238 100%)}
  .photo--closet{background:linear-gradient(90deg,#e4ddd2 0%,#b3607a 40%,#6d8fb0 70%,#a36c4a 100%)}
  .photo--patio{background:linear-gradient(180deg,#3c5a8a 0%,#e59a5c 30%,#9aa0a6 55%,#3f7a34 78%,#8d7a6c 100%)}

  .headline{left:5px;top:5px;width:430px;height:65px;background:var(--blue);color:var(--paper);
            font-family:"Montserrat",sans-serif;font-size:35px;display:flex;align-items:center;justify-content:center;letter-spacing:.3px;white-space:nowrap}
  .headline b{font-weight:800;margin-right:10px}
  .headline span{font-weight:500}

  .brand{background:var(--paper);border:1px solid var(--logo-border);display:flex;align-items:center;justify-content:center;gap:8px}
  .brand__mark{width:12px;height:12px;background:var(--blue);flex:none}
  .brand__name{font-family:"Tinos",serif;color:var(--blue);white-space:nowrap}
  .brand--front .brand__name{font-size:22px;letter-spacing:2px}
  .brand--back .brand__name{font-size:14px;letter-spacing:1px}

  .listing__title{left:228px;top:346px;width:207px;height:26px;background:var(--slate);color:var(--paper);
        font-family:"Oswald",sans-serif;font-weight:500;font-size:16px;letter-spacing:.6px;display:flex;align-items:center;padding-left:14px;white-space:nowrap}
  .listing__body{left:228px;top:375px;width:207px;height:107px;background:var(--blue-deep);color:var(--paper);
        font-family:"Roboto Condensed",sans-serif;font-weight:500;font-size:15px;padding:9px 0 0 16px}
  .listing__body ul{list-style:none}
  .listing__body li{line-height:23px}
  .listing__body li::before{content:"•";margin-right:12px}

  .summary{left:5px;top:485px;width:430px;height:55px;background:var(--blue);color:var(--paper);
        font-family:"Tinos",serif;font-size:6.3px;line-height:9px;padding:4px 8px}
  .summary__address{display:block;font-weight:700;font-size:8.5px;line-height:11px;margin-bottom:1px}

  .agent{right:5px;top:543px;width:140px;height:77px;background:var(--ink);color:var(--paper);
        font-family:"Oswald",sans-serif;text-align:right;padding:7px 9px;white-space:nowrap}
  .agent__name{font-size:22px;font-weight:600;line-height:26px}
  .agent__phone{font-family:"Roboto Condensed",sans-serif;font-size:17px;line-height:21px}
  .agent__email{font-family:"Roboto Condensed",sans-serif;font-size:9.5px;line-height:13px}

  .contact-bar{left:5px;top:275px;width:157px;height:38px;background:var(--blue);color:var(--paper);
        font-family:"Roboto Condensed",sans-serif;text-align:center;padding-top:3px;white-space:nowrap}
  .contact-bar__phone{font-size:16px;line-height:18px}
  .contact-bar__email{font-size:9px;line-height:12px}
</style>
</head>
<body>
<main class="canvas">

  <section class="page page--front" aria-label="Flyer front">
    <h1 class="block headline"><b>SELLING</b><span>MY HOME</span></h1>

    <div class="photo photo--garden" style="left:5px;top:73px;width:220px;height:132px" role="img" aria-label="Front of the home from the left with palm trees and lawn"></div>
    <div class="photo photo--porch" style="left:228px;top:73px;width:207px;height:132px" role="img" aria-label="Covered porch with tiled floor and ceiling fan"></div>

    <div class="block brand brand--front" style="left:5px;top:208px;width:220px;height:135px">
      <span class="brand__mark"></span>
      <span class="brand__name">ARDENT HOMES</span>
    </div>
    <div class="photo photo--aerial" style="left:228px;top:208px;width:207px;height:135px" role="img" aria-label="Aerial view of the home among trees"></div>

    <div class="photo photo--pool" style="left:5px;top:346px;width:220px;height:136px" role="img" aria-label="Screened pool and paver patio"></div>
    <div class="block listing__title">LISTING INFORMATION</div>
    <div class="block listing__body">
      <ul>
        <li>Price - $570,000</li>
        <li>Size – 2,307 SF</li>
        <li>3 bedrooms</li>
        <li>2 ½ bathrooms</li>
      </ul>
    </div>

    <p class="block summary"><span class="summary__address">4817 Birchwell Lane, Palm Beach Gardens, FL 33410</span>This impressive home boasts one of the largest yards in Palm Beach Gardens' most family friendly community, Willowmere. Enjoy the ultimate Florida lifestyle with a beautiful pool &amp; expanded patio areas - perfect for entertaining. Upgraded features throughout. Custom wood and ship lap details in all bathrooms and loft. New dark wood laminate flooring upstairs. New high-efficiency A/C units with smart thermostats. New pool pump and new heater controlled from your phone! Crown molding throughout. Walk-in closets. Quiet &amp; private cul-de-sac.</p>

    <div class="photo photo--roofs" style="left:5px;top:543px;width:430px;height:77px" role="img" aria-label="Aerial view with the home outlined among neighbouring roofs"></div>
    <div class="block agent">
      <div class="agent__name">Evan Marlow</div>
      <div class="agent__phone">561-555-0148</div>
      <div class="agent__email">evan@ardenthomes.com</div>
    </div>
  </section>

  <section class="page page--back" aria-label="Flyer back">
    <div class="photo photo--facade" style="left:9px;top:8px;width:425px;height:155px" role="img" aria-label="Front of the home with garage and palms"></div>

    <div class="block brand brand--back" style="left:5px;top:167px;width:157px;height:106px">
      <span class="brand__mark" style="width:9px;height:9px"></span>
      <span class="brand__name">ARDENT HOMES</span>
    </div>
    <div class="block contact-bar">
      <div class="contact-bar__phone">561-555-0148</div>
      <div class="contact-bar__email">evan@ardenthomes.com</div>
    </div>
    <div class="photo photo--living" style="left:167px;top:167px;width:267px;height:146px" role="img" aria-label="Bright living room with wood floors"></div>

    <div class="photo photo--room" style="left:9px;top:318px;width:103px;height:77px" role="img" aria-label="Bedroom"></div>
    <div class="photo photo--room" style="left:116px;top:318px;width:103px;height:77px" role="img" aria-label="Dining area"></div>
    <div class="photo photo--room" style="left:223px;top:318px;width:103px;height:77px" role="img" aria-label="Family room and kitchen"></div>
    <div class="photo photo--room" style="left:330px;top:318px;width:104px;height:77px" role="img" aria-label="Kitchen"></div>

    <div class="photo photo--closet" style="left:9px;top:398px;width:124px;height:219px" role="img" aria-label="Walk-in closet"></div>
    <div class="photo photo--patio" style="left:137px;top:398px;width:297px;height:219px" role="img" aria-label="Back patio and large yard at sunset"></div>
  </section>

</main>
</body>
</html>
```